Electrical flyer

We would like a flyer designed advertising "Does your house need a re-wire?" Potential fire hazards exist in houses constructed pre 1970. You're electrical cabling has insulation that corrodes leaving bare cables in the ceiling space. To find out more google VIR cable. To find out if you need a re-wire contact us on 0437 592 804 for a free assessment. We would like it to be quite confronting and grab peoples attention.

Target Market(s)

40-80 year olds

Industry/Entity Type

Electrical

Requirements
Must have
• Shock and confrontation, attention grabbing

```html
<!DOCTYPE html>
<html lang="en">
<head>
<meta charset="UTF-8">
<title>Norva Electrical – Re-wire Flyer</title>
<link rel="stylesheet" href="https://fonts.googleapis.com/css2?family=Raleway:wght@400;800&family=Roboto:wght@300&family=Roboto+Condensed:wght@300;700&display=swap">
<style>
  :root {
    --page-bg: #f2f3f3;
    --paper: #f4f5f5;
    --teal: #19a5a6;
    --teal-deep: #0d898b;
    --band-light: #c6dfe0;
    --ink-grey: #6f7272;
    --ink-dark: #111414;
    --photo-light: #eceded;
    --photo-mid: #d9dcdc;
  }
  * { margin: 0; padding: 0; box-sizing: border-box; }
  html, body {
    width: 1200px; height: 1037px; overflow: hidden;
    background: var(--page-bg);
  }
  .flyer {
    position: absolute; left: 260px; top: 38px;
    width: 680px; height: 960px;
    background: var(--paper);
    overflow: hidden;
    box-shadow: 0 10px 30px rgba(0,0,0,0.12);
  }
  .brand {
    position: absolute; top: 62px; left: 0; right: 0;
    text-align: center;
  }
  .brand-name {
    font-family: "Raleway", sans-serif; font-weight: 400;
    font-size: 40px; letter-spacing: 10px; color: var(--teal);
    text-transform: uppercase;
  }
  .brand-licence {
    margin-top: 14px;
    font-family: "Raleway", sans-serif; font-weight: 400;
    font-size: 16px; letter-spacing: 8px; color: var(--ink-grey);
  }
  .headline-band {
    position: absolute; top: 220px; left: 0; right: 0; height: 130px;
    background: var(--band-light);
    text-align: center; padding-top: 26px;
  }
  .headline-main {
    font-family: "Raleway", sans-serif; font-weight: 800;
    font-size: 50px; line-height: 1; color: var(--teal);
  }
  .headline-sub {
    font-family: "Raleway", sans-serif; font-weight: 800;
    font-size: 28px; line-height: 1.1; color: var(--ink-grey);
  }
  .intro {
    position: absolute; top: 380px; left: 90px; right: 90px;
    font-family: "Roboto", sans-serif; font-weight: 300;
    font-size: 19px; line-height: 1.5; color: var(--ink-grey);
    text-align: center;
  }
  .photo {
    position: absolute; top: 500px; left: 0; right: 0; height: 340px;
    background: linear-gradient(180deg, var(--photo-light) 0%, var(--photo-mid) 100%);
  }
  .cta-band {
    position: absolute; bottom: 0; left: 0; right: 0; height: 130px;
    background: var(--teal-deep);
    text-align: center; padding-top: 30px;
    font-family: "Roboto Condensed", sans-serif;
  }
  .cta-line {
    font-weight: 300; font-size: 22px; color: #ffffff;
    text-transform: uppercase;
  }
  .cta-offer {
    font-weight: 300; font-size: 34px; color: var(--ink-dark);
    text-transform: uppercase;
  }
  .cta-phone { font-weight: 700; }
</style>
</head>
<body>
  <article class="flyer">
    <header class="brand">
      <div class="brand-name">Norva Electrical</div>
      <div class="brand-licence">EC58203</div>
    </header>

    <section class="headline-band">
      <h1 class="headline-main">DOES YOUR</h1>
      <h2 class="headline-sub">HOUSE NEED A RE-WIRE?</h2>
    </section>

    <p class="intro">
      Potential fire hazards exist in houses constructed pre 1970. You're electrical cabling has insulation that corrodes leaving bare cables in the ceiling space. To find out more google VIR cable.
    </p>

    <div class="photo" role="img" aria-label="Photo of a man and a woman sitting face to face, chins resting on their hands, deep in thought"></div>

    <footer class="cta-band">
      <div class="cta-line">To find out if you need a re-wire contact us on</div>
      <div class="cta-offer"><span class="cta-phone">0437 592 804</span> for a free assessment.</div>
    </footer>
  </article>
</body>
</html>
```